Flyer für selbstständigen Finanzierungsvermittler  für Baufinanzierungen
Flyer für selbstständigen Finanzierungsvermittler für Baufinanzierungen
Zielgruppe
seit 1999 selbstständiger Finanzierungsvermittler für Baufinanzierungen.
ich arbeite für (nicht angestellt) ein Maklerbüro in Schorndorf, hier wurde vor Jahren ein Flyer konzepiert.
Zukünftiger Flyer soll von Immobilienmaklern Interessenten ausgehändigt oder in Kundenmappe VEK-Maklerbüro beigelegt werden.
Aufgabenstellung
- der beigefügte Flyer von Lukas Brandel hat schon sehr viel von dem, was ich mir das vorstelle
- die Farben des Maklerbüros sind Blau und weiß, kann aber auch ganz anders entworfen werden
- Es soll ein DinA 4 Flyer werden, ebenso die PDF-Datei hierzu
- Adressfeld: Stefan Kurlen, Baufinanzierungsspezialist, Bankkaufmann, Haldenweg 17, 73814 Lindenbach, Mobil 0171 546 7183, stefan@kurlen48.de
Text für den Flyer, anlehnend an beileigende:
- Längjährige Erfahrung
- Vergleich von über 300 Banken
- Top Konditionen, bis zu 40 Jahre Zinsbindung
- Beratung vor Ort, auch per Viseo und Telefon möglich
- rasche Zusage, aufgrund persönlichem Kontakt zu Entscheidungsträgern der Bank
mitgelieferte Bilder dürfen natürlich zugeschnitten werden (nur bis Brust) oder weniger Hintergrund, etc.

```html
<!DOCTYPE html>
<html lang="de">
<head>
<meta charset="utf-8">
<title>Stefan Kurlen – Baufinanzierungsspezialist</title>
<link href="https://fonts.googleapis.com/css2?family=Barlow:wght@400;500;800&family=Amatic+SC:wght@700&display=swap" rel="stylesheet">
<style>
  :root {
    --navy: #0d2955;
    --mid-blue: #2389b9;
    --soft-blue: #8fb6d8;
    --lilac-blue: #8fa9d0;
    --cyan-band: #86c8d8;
    --tick: #8fd0e0;
    --ink: #111a22;
    --paper: #ffffff;
    --on-navy: #eef3f8;
  }
  * { margin: 0; padding: 0; box-sizing: border-box; }
  html, body { width: 849px; height: 1200px; overflow: hidden; background: var(--paper); }
  .flyer {
    position: relative; width: 849px; height: 1200px; overflow: hidden;
    font-family: "Barlow", sans-serif; color: var(--ink);
  }
  .backdrop { position: absolute; inset: 0; }
  .contact {
    position: absolute; left: 602px; top: 127px;
    font-size: 19px; line-height: 22px; color: var(--ink);
  }
  .contact .name { font-weight: 800; font-size: 21px; }
  .contact .gap { margin-top: 8px; }
  .greeting {
    position: absolute; left: 540px; top: 636px; width: 300px;
    font-family: "Amatic SC", sans-serif; font-weight: 700;
    font-size: 40px; line-height: 37px; color: var(--navy);
    text-transform: uppercase; text-align: center; transform: rotate(-4deg);
  }
  .headline {
    position: absolute; left: 55px; top: 716px;
    font-weight: 800; font-size: 54px; letter-spacing: 3px; line-height: 60px;
    color: var(--ink); white-space: nowrap;
  }
  .role {
    position: absolute; left: 55px; top: 782px;
    font-size: 31px; line-height: 36px; font-weight: 400; color: var(--ink);
  }
  .benefit {
    position: absolute; font-size: 22px; line-height: 27px; font-weight: 500;
    color: var(--on-navy); white-space: nowrap;
  }
  .benefit .line { display: block; }
  .benefit .tick { color: var(--tick); font-weight: 800; margin-right: 10px; }
</style>
</head>
<body>
<main class="flyer">
  <svg class="backdrop" width="849" height="1200" viewBox="0 0 849 1200">
    <defs>
      <linearGradient id="photoTone" x1="0" y1="0" x2="1" y2="1">
        <stop offset="0" stop-color="#dfeaf1"/>
        <stop offset="0.6" stop-color="#eef4f8"/>
        <stop offset="1" stop-color="#ffffff"/>
      </linearGradient>
      <linearGradient id="stripeFade" x1="0" y1="0" x2="0" y2="1">
        <stop offset="0" stop-color="#2a8fc0"/>
        <stop offset="1" stop-color="#2486b6"/>
      </linearGradient>
    </defs>
    <rect x="0" y="0" width="849" height="857" fill="url(#photoTone)"/>
    <rect x="60" y="40" width="560" height="817" fill="#c9d6df" opacity="0.55" role="img" aria-label="Porträtfoto des Baufinanzierungsspezialisten im dunklen Sakko, an eine Wand gelehnt"/>
    <polygon points="849,262 849,439 751,606 627,617" fill="var(--soft-blue)"/>
    <polygon points="677,339 789,339 293,1200 175,1200" fill="var(--mid-blue)"/>
    <polygon points="849,439 849,760 640,800 751,606" fill="var(--mid-blue)"/>
    <polygon points="560,760 700,740 600,857 490,857" fill="var(--lilac-blue)"/>
    <rect x="0" y="679" width="849" height="178" fill="var(--cyan-band)" opacity="0.72"/>
    <rect x="0" y="857" width="849" height="343" fill="var(--navy)"/>
    <polygon points="375,857 493,857 293,1200 175,1200" fill="url(#stripeFade)"/>
    <polygon points="541,627 849,601 849,753 554,779" fill="var(--paper)"/>
  </svg>

  <section class="contact">
    <p class="name">Stefan Kurlen</p>
    <p>Bankkaufmann</p>
    <p class="gap">Haldenweg 17<br>73814 Lindenbach</p>
    <p class="gap">Mobil 0171 546 7183</p>
    <p class="gap">stefan@kurlen48.de</p>
  </section>

  <p class="greeting">Ich freue mich<br>auf ein persönliches<br>Gespräch mit Ihnen.</p>

  <h1 class="headline">STEFAN KURLEN</h1>
  <p class="role">Ihr Baufinanzierungsspezialist</p>

  <p class="benefit" style="left:55px;top:910px"><span class="tick">✓</span>Langjährige Erfahrung</p>
  <p class="benefit" style="left:55px;top:956px"><span class="line"><span class="tick">✓</span>Vergleich von über</span><span class="line" style="margin-left:26px">300 Banken</span></p>

  <p class="benefit" style="left:481px;top:912px"><span class="line"><span class="tick">✓</span>Top Konditionen,</span><span class="line" style="margin-left:17px">bis zu 40 Jahre Zinsbindung</span></p>
  <p class="benefit" style="left:445px;top:983px"><span class="line"><span class="tick">✓</span>Beratung vor Ort, auch per Video</span><span class="line" style="margin-left:10px">und Telefon möglich</span></p>
  <p class="benefit" style="left:402px;top:1054px"><span class="line"><span class="tick">✓</span>rasche Zusage, aufgrund</span><span class="line" style="margin-left:11px">persönlichem Kontakt</span><span class="line" style="margin-left:-4px">zu Entscheidungsträgern der Bank</span></p>
</main>
</body>
</html>
```